Photography Business, Business Card

Looking for a unique cutting edge card that takes advantage of the latest printing technologies. Please review this site for all the options they office: https://plumeprints.example. If you can think it they can do it. And if you have an idea and do not know if they can do it, I will check into it.
Updates

Target Market(s)

People and places I took images of and future clients.

Industry/Entity Type

Photography

Contact Information for Business Card

Name, cell & email. Colin Hartley, chartley@kvnphoto.example, 318-742-9061

Colors

Designer to choose only greyscale colors for use in the design.

Requirements
Must have
• 100% cutting edge. Is so great, those I hand it to always show it to someone else. A piece of art.
Nice to have
• Blacks, silvers, greys, some red. Maybe other colors?

```html
<!DOCTYPE html>
<html lang="en">
<head>
<meta charset="utf-8">
<title>Colin Hartley Photography – Business Card</title>
<link rel="stylesheet" href="https://fonts.googleapis.com/css2?family=Mulish:wght@700&display=swap">
<style>
  :root {
    --backdrop: #d8311f;
    --card-black: #1c1c1f;
    --card-black-light: #2b2b2f;
    --line-white: #ffffff;
    --line-red: #d8202a;
    --text-white: #ffffff;
    --mark-dark: #26262a;
    --mark-red: #5a1c20;
  }
  html, body {
    margin: 0;
    padding: 0;
    overflow: hidden;
  }
  body {
    width: 1200px;
    height: 1156px;
    background: var(--backdrop);
    position: relative;
    font-family: "Mulish", sans-serif;
  }
  .business-card {
    position: absolute;
    left: 100px;
    top: 240px;
    width: 1000px;
    height: 676px;
  }
  .card-surface { fill: url(#leather-tone); }
  .mark-area { fill: url(#mark-tone); }
  .frame-white, .band-white {
    fill: none;
    stroke: var(--line-white);
    stroke-width: 5;
  }
  .frame-red, .band-red {
    fill: none;
    stroke: var(--line-red);
    stroke-width: 5;
  }
  .contact-text {
    fill: var(--text-white);
    font-family: "Mulish", sans-serif;
    font-weight: 700;
    text-anchor: middle;
  }
  .phone-number { font-size: 18px; }
  .email-address { font-size: 20px; }
  .studio-name {
    fill: var(--text-white);
    font-family: "Mulish", sans-serif;
    font-weight: 700;
    font-size: 22px;
    text-anchor: middle;
  }
</style>
</head>
<body>
  <svg class="business-card" viewBox="0 0 766 518" xmlns="http://www.w3.org/2000/svg">
    <defs>
      <linearGradient id="leather-tone" x1="0" y1="0" x2="1" y2="1">
        <stop offset="0" stop-color="var(--card-black-light)"/>
        <stop offset="1" stop-color="var(--card-black)"/>
      </linearGradient>
      <radialGradient id="mark-tone" cx="0.5" cy="0.5" r="0.5">
        <stop offset="0" stop-color="var(--mark-dark)"/>
        <stop offset="0.8" stop-color="var(--mark-red)"/>
        <stop offset="1" stop-color="var(--mark-dark)"/>
      </radialGradient>
    </defs>

    <rect class="card-surface" x="0" y="0" width="766" height="518" rx="24" role="img" aria-label="Black leather texture card surface"/>

    <path class="frame-white" d="M80,44 Q42,48 42,85 L42,430 Q42,462 80,466"/>
    <path class="frame-red" d="M688,44 Q722,48 722,85 L722,430 Q722,462 688,468"/>

    <path class="band-red" d="M54,168 H214"/>
    <path class="band-white" d="M544,168 H710"/>
    <path class="band-white" d="M48,350 H214"/>
    <path class="band-red" d="M544,350 H720"/>

    <circle class="mark-area" cx="379" cy="260" r="162" role="img" aria-label="Red and white camera lens line illustration"/>

    <text class="studio-name" x="383" y="268">Colin Hartley Photography</text>

    <text class="contact-text phone-number" x="382" y="62">318-742-9061</text>
    <text class="contact-text email-address" x="383" y="468">chartley@kvnphoto.example</text>
  </svg>
</body>
</html>
```